Owen Tasker Studios Business Card

Looking for a clear, modern, elegant, sharp business card that conveys a professional yet edgy image to my business as a wedding, portrait, and travel photographer. Would like something that looks vintage yet modern. Need a new business card to grow my business. We are growing the business for Wedding and Event Photography as well as fine art Photography. (Mostly Landscapes)
Updates

I’m looking through designs now but I have a new logo that i want using please.

New logo uploaded please redesign using that

PLEASE ALL DESIGNERS LOOK IN BRIEF FOR NEW LOGO

Target Market(s)

Brides, Grooms, Families with Kids, People looking for Fine Art Photography Artwork

Industry/Entity Type

Photographer

Contact Information for Business Card

Unsure

Font styles to use
Serif

Colors

Designer to choose colors to be used in the design.

Requirements
Must have
• My Website:
• http://taskerlens.examplefolio.net
• Phone:
• 323-481-5206
• Email:
• owentaskerlens@mailbox-example.net
Nice to have
• Would like a sort of shine on the printing finish.
• I like black I think it looks good on a business card.
• Can try working with my logo (png that I've attached)

```html
<!DOCTYPE html>
<html lang="en">
<head>
<meta charset="utf-8">
<title>Owen Tasker Studios Business Card</title>
<link rel="stylesheet" href="https://fonts.googleapis.com/css2?family=Raleway:wght@300&family=Oswald:wght@500&family=Open+Sans:wght@400&display=swap">
<style>
  :root {
    --backdrop: #5a3f2c;
    --card: #202020;
    --card-edge: #1a1a1a;
    --mark: #8f8f8f;
    --mark-sub: #8a8a8a;
    --name: #9a9a9a;
    --text: #a9a9a9;
    --rule: #7a7a7a;
  }
  * { margin: 0; padding: 0; box-sizing: border-box; }
  html, body {
    width: 1200px;
    height: 1000px;
    overflow: hidden;
    background: var(--backdrop);
  }
  .canvas {
    position: relative;
    width: 1200px;
    height: 1000px;
  }
  .card {
    position: absolute;
    left: 266px;
    width: 666px;
    height: 397px;
    background: var(--card);
    box-shadow: 0 4px 14px rgba(0,0,0,0.45);
  }
  .card--front { top: 74px; }
  .card--back { top: 533px; }

  .wordmark {
    position: absolute;
    left: 0;
    right: 0;
    text-align: center;
    font-family: "Raleway", sans-serif;
    font-weight: 300;
    color: var(--mark);
  }
  .wordmark__name {
    top: 164px;
    font-size: 37px;
    letter-spacing: 9px;
    padding-left: 9px;
  }
  .wordmark__sub {
    top: 222px;
    font-size: 14px;
    letter-spacing: 6px;
    padding-left: 6px;
    color: var(--mark-sub);
  }

  .identity {
    position: absolute;
    right: 390px;
    top: 166px;
    text-align: right;
  }
  .identity__name {
    font-family: "Oswald", sans-serif;
    font-weight: 500;
    font-size: 25px;
    line-height: 30px;
    letter-spacing: -0.5px;
    color: var(--name);
  }
  .identity__role {
    font-family: "Open Sans", sans-serif;
    font-size: 15px;
    line-height: 20px;
    color: var(--text);
  }
  .divider {
    position: absolute;
    left: 296px;
    top: 169px;
    width: 1px;
    height: 56px;
    background: var(--rule);
  }
  .contacts {
    position: absolute;
    left: 312px;
    top: 165px;
    list-style: none;
    font-family: "Open Sans", sans-serif;
    font-size: 15px;
    line-height: 20.5px;
    color: var(--text);
  }
  .contacts li {
    display: flex;
    align-items: center;
    gap: 7px;
    white-space: nowrap;
  }
  .contacts svg {
    width: 13px;
    height: 13px;
    flex: none;
    stroke: var(--text);
    fill: none;
    stroke-width: 1.3;
  }
</style>
</head>
<body>
<main class="canvas">
  <section class="card card--front" aria-label="Card front">
    <div class="wordmark wordmark__name">OWEN TASKER</div>
    <div class="wordmark wordmark__sub">STUDIOS</div>
  </section>

  <section class="card card--back" aria-label="Card back">
    <div class="identity">
      <div class="identity__name">OWEN TASKER</div>
      <div class="identity__role">Photographer</div>
    </div>
    <div class="divider"></div>
    <ul class="contacts">
      <li>
        <svg viewBox="0 0 16 16" aria-hidden="true"><path d="M3 1.5l2.5 0 1.2 3.3-1.6 1.1c.8 1.8 2.2 3.2 4 4l1.1-1.6 3.3 1.2 0 2.5c0 .8-.7 1.5-1.5 1.5C6.6 13.5 1.5 8.4 1.5 3 1.5 2.2 2.2 1.5 3 1.5z"/></svg>
        <span>323-481-5206</span>
      </li>
      <li>
        <svg viewBox="0 0 16 16" aria-hidden="true"><rect x="1.5" y="3.5" width="13" height="9"/><path d="M1.5 3.5l6.5 5 6.5-5"/></svg>
        <span>owentaskerlens@mailbox-example.net</span>
      </li>
      <li>
        <svg viewBox="0 0 16 16" aria-hidden="true"><circle cx="8" cy="8" r="6.5"/><ellipse cx="8" cy="8" rx="2.8" ry="6.5"/><path d="M1.5 8h13M2.5 4.8h11M2.5 11.2h11"/></svg>
        <span>taskerlens.examplefolio.net</span>
      </li>
    </ul>
  </section>
</main>
</body>
</html>
```